Stationery Design Project - KLVA Partners

Business Cards
Size: 90mm x 55mm
Letterhead
Size: A4 - 210mm x 297mm
With Compliments Slip
Size: DL - 210mm x 99mm
Presentation Folder
Size: A4

KLVA Partners
website: www.klvapartners.com.au (Under construction)
Offices: *Perth *Brisbane * Seoul

A company that supply Safety consultantcy services

Industry/Entity Type

Business

```html
<!DOCTYPE html>
<html lang="en">
<head>
<meta charset="utf-8">
<title>KLVA Partners – Stationery</title>
<link rel="stylesheet" href="https://fonts.googleapis.com/css2?family=Didact+Gothic&family=Montserrat:wght@700&display=swap">
<style>
  :root {
    --backdrop: #abaab0;
    --paper: #ffffff;
    --brand-blue: #0a63b0;
    --mark-blue: #8fb4c8;
    --mark-square: #5d8fae;
    --text-grey: #5e6166;
    --art-light: #eef1f4;
    --art-mid: #dde4ea;
    --art-tint: #d3e6f2;
  }
  * { box-sizing: border-box; margin: 0; padding: 0; }
  html, body { width: 1200px; height: 848px; overflow: hidden; }
  body {
    background: var(--backdrop);
    font-family: "Didact Gothic", "Century Gothic", sans-serif;
    color: var(--text-grey);
    position: relative;
  }
  .sheet {
    position: absolute;
    background: var(--paper);
    overflow: hidden;
    box-shadow: 0 2px 8px rgba(0,0,0,.25);
  }
  .brand-band {
    position: absolute;
    left: 0; right: 0; bottom: 0;
    background: var(--brand-blue);
  }
  .brand {
    position: absolute;
    display: flex;
    align-items: center;
    gap: 6px;
    color: var(--mark-blue);
    white-space: nowrap;
  }
  .brand-square { background: var(--mark-square); flex: none; }
  .artwork {
    position: absolute;
    background: linear-gradient(135deg, rgba(255,255,255,0) 0%, var(--art-light) 30%, var(--art-tint) 55%, var(--art-mid) 80%, var(--art-light) 100%);
    -webkit-mask-image: radial-gradient(ellipse at 65% 60%, #000 45%, transparent 80%);
    mask-image: radial-gradient(ellipse at 65% 60%, #000 45%, transparent 80%);
  }
  .contact { position: absolute; line-height: 1.22; white-space: nowrap; }
  .holder { position: absolute; white-space: nowrap; }
  .holder-name {
    font-family: "Montserrat", Arial, sans-serif;
    font-weight: 700;
    color: var(--brand-blue);
    font-size: 6px;
  }
  .holder-role { font-size: 6px; color: var(--text-grey); }
  .card-url {
    position: absolute;
    left: 0; right: 0;
    text-align: center;
    font-family: "Montserrat", Arial, sans-serif;
    font-weight: 700;
    font-size: 6px;
    color: var(--brand-blue);
  }

  /* Business cards sit above the letterhead */
  .card { width: 216px; height: 131px; z-index: 2; }
  .card .brand-band { height: 6px; }
  .card-front .brand { left: 42px; top: 52px; font-size: 15px; }
  .card-front .brand-square { width: 26px; height: 26px; }
  .card-front .card-url { top: 111px; }

  .card-back .brand { font-size: 11px; gap: 4px; }
  .card-back .brand-square { width: 20px; height: 20px; }
  .card-back .contact { font-size: 6px; }

  /* Letterhead */
  .letterhead { left: 334px; top: 68px; width: 503px; height: 714px; z-index: 1; }
  .letterhead .brand { left: 24px; top: 32px; font-size: 22px; gap: 8px; }
  .letterhead .brand-square { width: 40px; height: 40px; }
  .letterhead .artwork { left: 90px; top: 300px; width: 413px; height: 400px; }
  .letterhead .contact { left: 22px; top: 648px; font-size: 9.5px; }
  .letterhead .brand-band { height: 14px; }

  /* Compliments slip */
  .comp-slip { left: 657px; top: 308px; width: 503px; height: 237px; z-index: 3; }
  .comp-slip .brand { left: 24px; top: 24px; font-size: 22px; gap: 8px; }
  .comp-slip .brand-square { width: 44px; height: 44px; }
  .comp-slip .artwork { left: 280px; top: 60px; width: 223px; height: 168px; }
  .comp-slip .contact { left: 22px; top: 173px; font-size: 9.5px; }
  .comp-slip .brand-band { height: 10px; }
</style>
</head>
<body>

  <!-- Letterhead -->
  <section class="sheet letterhead">
    <div class="artwork" role="img" aria-label="Large faded abstract 3D cube blocks in white and pale blue"></div>
    <div class="brand"><span class="brand-square"></span>KLVA Partners</div>
    <div class="contact">
      555-0142 / 955000187<br>
      info@klvapartners.com<br>
      www.klvapartners.com.au<br>
      48, Av. Las Palmeras - 7200 Lima Perú
    </div>
    <div class="brand-band"></div>
  </section>

  <!-- Business card front, upper -->
  <section class="sheet card card-front" style="left:43px; top:231px;">
    <div class="brand"><span class="brand-square"></span>KLVA Partners</div>
    <p class="card-url">www.klvapartners.com.au</p>
    <div class="brand-band"></div>
  </section>

  <!-- Business card back, name left -->
  <section class="sheet card card-back" style="left:278px; top:231px;">
    <div class="artwork" role="img" aria-label="Faded abstract 3D cube blocks in white and pale blue" style="left:0; top:20px; width:140px; height:105px;"></div>
    <div class="brand" style="left:88px; top:9px;"><span class="brand-square"></span>KLVA Partners</div>
    <div class="holder" style="left:19px; top:59px; text-align:center;">
      <p class="holder-name">Nombre Apellido Apellido</p>
      <p class="holder-role">Cargo</p>
    </div>
    <div class="contact" style="right:12px; top:92px; text-align:right;">
      555-0142 / 955000187<br>
      info@klvapartners.com<br>
      www.klvapartners.com.au<br>
      48, Av. Las Palmeras - 7200 Lima Perú
    </div>
    <div class="brand-band"></div>
  </section>

  <!-- Business card front, lower -->
  <section class="sheet card card-front" style="left:43px; top:393px;">
    <div class="brand"><span class="brand-square"></span>KLVA Partners</div>
    <p class="card-url">www.klvapartners.com.au</p>
    <div class="brand-band"></div>
  </section>

  <!-- Business card back, name right -->
  <section class="sheet card card-back" style="left:278px; top:393px;">
    <div class="artwork" role="img" aria-label="Faded abstract 3D cube blocks in white and pale blue" style="left:96px; top:20px; width:120px; height:105px;"></div>
    <div class="brand" style="left:11px; top:9px;"><span class="brand-square"></span>KLVA Partners</div>
    <div class="holder" style="right:12px; top:59px; text-align:center;">
      <p class="holder-name">Nombre Apellido Apellido</p>
      <p class="holder-role">Cargo</p>
    </div>
    <div class="contact" style="left:12px; top:84px;">
      555-0142 / 955000187<br>
      info@klvapartners.com<br>
      www.klvapartners.com.au<br>
      48, Av. Las Palmeras - 7200 Lima Perú
    </div>
    <div class="brand-band"></div>
  </section>

  <!-- With compliments slip -->
  <section class="sheet comp-slip">
    <div class="artwork" role="img" aria-label="Faded abstract 3D cube blocks in white and pale blue"></div>
    <div class="brand"><span class="brand-square"></span>KLVA Partners</div>
    <div class="contact">
      555-0142 / 955000187<br>
      info@klvapartners.com<br>
      www.klvapartners.com.au<br>
      48, Av. Las Palmeras - 7200 Lima Perú
    </div>
    <div class="brand-band"></div>
  </section>

</body>
</html>
```